A start-up named "Corvath Therapeutics" - needs a new PowerPoint design

We need a new PowerPoint Design for an early-stage start-up named "Corvath Therapeutics" seeking to disrupt the current approach towards drug discovery within aging disorders.

We would like to build on Corvath's legacy, the founder of the modern science of genetics, by employing a multidisciplinary approach, experimenting, and providing elderly patients the attention they deserve.

We have selected the suffix "therapeutics" intentionally as it stands for (a medicine) the treatment of disease; the science of healing. Alzheimer’s treatment is a huge, urgent, unmet need:
- Shift from a disease-management system to a preventive medicine system
- Focus on increasing the health span, not only the life span

Target Market(s)

Pharma/ Biotech Executives Medical Institutions Healthcare professionals (MDs, nurses, payors, pharmacists, etc.) Patients

Industry/Entity Type

Healthcare

Other font styles liked:
• Celias

Colors
0054AA
0677BA
7BADD7
CADEEF
E8F1F8
E54698
E96AAD
F1A4CE
F9D9EA
FCEFF6
A7469A
B969AE
D3A5CF
EDDBEB
F8F0F9
6B429C
8869AF
B7A5CE
E3DAEB
F3F0F8

Requirements
Must have
• - differentiate from other companies named after Corvath - differentiate from other Pharma/ Biotech companies
Nice to have
• simplicity/ minimalist logo vivid colors gradient 3D Life-Sciences inspired Simple geometry Balance
Should not have
• mascot/ emblem watermark logo animated ink style nature-inspired inventive typography artistic chaos

```html
<!DOCTYPE html>
<html lang="en">
<head>
<meta charset="utf-8">
<title>Corvath Therapeutics – Slide Deck</title>
<link href="https://fonts.googleapis.com/css2?family=Poppins:wght@400;500;600;700&display=swap" rel="stylesheet">
<style>
:root{
  --cyan:#3fc3ef;
  --blue:#2c6fd6;
  --navy:#2b2f8c;
  --purple:#7d35a3;
  --violet:#8a3aa0;
  --magenta:#b5289b;
  --ink:#1e1e24;
  --grey:#6b6b73;
  --page:#dcdcdc;
  --light:#f2f2f4;
}
*{margin:0;padding:0;box-sizing:border-box}
html,body{width:785px;height:1200px;overflow:hidden;background:var(--page);font-family:"Poppins",sans-serif;color:var(--ink)}
.deck{display:grid;grid-template-columns:repeat(3,252px);grid-auto-rows:142px;column-gap:7.5px;row-gap:7px;padding:7px}
.slide{position:relative;background:#fff;overflow:hidden}

/* brand */
.brand{display:flex;align-items:center;gap:3px;font-weight:500;white-space:nowrap}
.brand i{display:block;width:9px;height:9px;border:1.3px solid currentColor}
.brand span{font-size:8px;letter-spacing:.2px}

/* covers */
.cover{color:#fff;text-align:center}
.cover .brand{position:absolute;top:28px;left:50%;transform:translateX(-50%)}
.cover h1{position:absolute;top:57px;left:0;right:0;font-size:15.5px;line-height:15px;font-weight:600}
.cover .sub{position:absolute;top:90px;left:0;right:0;font-size:6px;font-weight:400}
.pill{position:absolute;top:115px;left:50%;transform:translateX(-50%);width:54px;height:9px;border-radius:5px;font-size:3.6px;line-height:9px;font-weight:600;color:#fff;text-align:center}
.pill.pink{background:var(--magenta)}
.pill.sky{background:var(--cyan)}
.pill.grad{background:linear-gradient(90deg,var(--cyan),var(--navy))}
.photo-dark{background:linear-gradient(120deg,#3a3a3a,#6b6b6b 45%,#2a2a2a)}
.photo-pink{background:linear-gradient(135deg,#c47ab8,#9e3aa6 55%,#6b2a8f)}
.photo-blue{background:linear-gradient(135deg,#5ea8c8,#3f6fb8 50%,#3a3aa0)}
.net-grad{background:linear-gradient(135deg,#3fbdee,#6b5fc4 50%,#a3379e)}
.dark-grad{background:linear-gradient(160deg,#2a2a2c,#474749)}
.cover.white{color:var(--ink)}
.cover.white .brand{color:var(--purple)}
.cover.side{text-align:left;background:linear-gradient(135deg,#3fbdee,#7a55c0 55%,#a3379e)}
.cover.side .brand{left:15px;top:34px;transform:none}
.cover.side h1{left:15px;top:58px;font-size:13px;line-height:13px}
.cover.side .sub{left:15px;top:87px;font-size:4.5px}
.cover.side .pill{left:15px;top:104px;transform:none}
.fill{position:absolute;inset:0}

/* content slides */
.title{position:absolute;left:14px;top:20px;font-size:11.5px;font-weight:500}
.title::after{content:"";display:block;width:11px;height:2px;background:var(--cyan);margin-top:3px}
.title.center{left:0;right:0;text-align:center}
.title.center::after{margin:3px auto 0}
.lorem{font-size:3.1px;line-height:4.2px;color:var(--grey)}
.pname{font-size:3.6px;font-weight:600;color:var(--magenta)}

/* footer */
.foot{position:absolute;left:10px;right:10px;bottom:4px;height:6px;display:flex;align-items:center;gap:4px}
.foot .brand{color:var(--purple)}
.foot .brand i{width:5px;height:5px;border-width:.8px}
.foot .brand span{font-size:3.6px}
.foot .bar{flex:1;height:4px;background:linear-gradient(90deg,var(--cyan),var(--blue) 60%,var(--navy));transform:skewX(-30deg);font-size:2px;color:#fff;text-align:center;line-height:4px;letter-spacing:.3px}
.foot .num{width:14px;height:4px;background:var(--magenta);transform:skewX(-30deg);font-size:2.4px;line-height:4px;color:#fff;text-align:center}

.icon{position:absolute;width:9px;height:9px;border:1px solid var(--navy)}
.ring{position:absolute;width:13px;height:13px;border-radius:50%;background:#fff;box-shadow:0 0 3px rgba(0,0,0,.2)}
.ring::after{content:"";position:absolute;inset:3.5px;border-radius:50%;border:1px solid var(--violet)}

.stat{position:absolute;top:74px;width:60px;text-align:center}
.stat b{display:block;font-size:11px;color:var(--violet);font-weight:600}
.box{position:absolute;color:#fff;padding:6px 7px;border-radius:1px}
.box h3{font-size:5.2px;font-weight:500;margin-bottom:4px}
.box .lorem{color:rgba(255,255,255,.8)}

.card{position:absolute;top:58px;width:57px;height:54px;color:#fff;text-align:center;padding:18px 5px 0}
.card h4{font-size:3.8px;font-weight:600;margin-bottom:2px}
.card .lorem{color:rgba(255,255,255,.85);font-size:2.9px;line-height:3.8px}

table{position:absolute;left:20px;top:42px;width:212px;border-collapse:collapse;font-size:3.2px;text-align:center}
th{background:var(--cyan);color:#fff;height:10px;font-weight:600}
td{height:11.8px;color:var(--grey)}
td:first-child{background:var(--violet);color:#fff;font-weight:600}
tr:nth-child(even) td:not(:first-child){background:#f2f2f4}
tbody tr:last-child td{border-bottom:1px solid #f0a070}

.contact{position:absolute;left:34px;width:67px;height:16px;background:#fff;font-size:2.8px;color:var(--grey);display:flex;align-items:center;gap:5px;padding-left:6px;box-shadow:0 0 3px rgba(0,0,0,.08)}
</style>
</head>
<body>
<main class="deck">

<!-- 1 -->
<section class="slide cover">
  <div class="fill photo-dark" role="img" aria-label="Photo of two hands reaching toward each other"></div>
  <div class="brand"><i></i><span>Corvath Therapeutics</span></div>
  <h1>Presentation<br>Title Goes Here</h1>
  <p class="sub">Sub Title Goes Here</p>
  <div class="pill pink">Oct 2021</div>
</section>
<!-- 2 -->
<section class="slide cover">
  <div class="fill photo-pink" role="img" aria-label="Photo of two hands reaching, tinted pink and purple"></div>
  <div class="brand"><i></i><span>Corvath Therapeutics</span></div>
  <h1>Presentation<br>Title Goes Here</h1>
  <p class="sub">Sub Title Goes Here</p>
  <div class="pill pink">Jan 2022</div>
</section>
<!-- 3 -->
<section class="slide cover">
  <div class="fill photo-blue" role="img" aria-label="Photo of two hands reaching, tinted blue"></div>
  <div class="brand"><i></i><span>Corvath Therapeutics</span></div>
  <h1>Presentation<br>Title Goes Here</h1>
  <p class="sub">Sub Title Goes Here</p>
  <div class="pill pink">Jan 2022</div>
</section>
<!-- 4 -->
<section class="slide cover">
  <div class="fill net-grad" role="img" aria-label="Gradient background with a molecular network pattern"></div>
  <div class="brand"><i></i><span>Corvath Therapeutics</span></div>
  <h1>Presentation<br>Title Goes Here</h1>
  <p class="sub">Sub Title Goes Here</p>
  <div class="pill sky">Oct 2021</div>
</section>
<!-- 5 -->
<section class="slide cover dark-grad">
  <div class="brand"><i></i><span>Corvath Therapeutics</span></div>
  <h1>Presentation<br>Title Goes Here</h1>
  <p class="sub">Sub Title Goes Here</p>
  <div class="pill grad">Oct 2021</div>
</section>
<!-- 6 -->
<section class="slide cover white">
  <div class="brand" style="top:32px"><i></i><span>Corvath Therapeutics</span></div>
  <h1 style="top:60px">Presentation<br>Title Goes Here</h1>
  <p class="sub" style="top:90px">Sub Title Goes Here</p>
  <div class="pill grad" style="top:108px">Oct 2021</div>
</section>
<!-- 7 -->
<section class="slide cover side">
  <div class="brand"><i></i><span>Corvath Therapeutics</span></div>
  <h1>Presentation<br>Title Goes Here</h1>
  <p class="sub">Sub Title Goes Here</p>
  <div class="pill sky">Oct 2021</div>
</section>

<!-- 8 -->
<section class="slide">
  <h2 class="title">Title And Body Slide</h2>
  <footer class="foot"><div class="brand"><i></i><span>Corvath</span></div><div class="bar">CORVATH | Copyright ©</div><div class="num">8</div></footer>
</section>
<!-- 9 -->
<section class="slide">
  <h2 class="title">Title And Body Slide</h2>
  <div class="lorem" style="position:absolute;left:14px;right:16px;top:46px">
    <p style="margin-bottom:4px">Lorem ipsum dolor sit amet, consectetur adipiscing elit, sed do eiusmod tempor incididunt ut labore et dolore magna aliqua. Ut enim ad minim veniam, quis nostrud exercitation ullamco laboris nisi ut aliquip ex ea commodo.</p>
    <p style="margin-bottom:4px">Lorem ipsum dolor sit amet, consectetur adipiscing elit, sed do eiusmod tempor incididunt ut labore et dolore magna aliqua. Lorem ipsum dolor sit amet, consectetur adipiscing elit, sed do eiusmod tempor incididunt ut labore et dolore magna aliqua. Ut enim ad minim veniam.</p>
    <p>Lorem ipsum dolor sit amet, consectetur adipiscing elit, sed do eiusmod tempor incididunt ut labore et dolore magna aliqua. Lorem ipsum dolor sit amet, consectetur adipiscing elit, sed do eiusmod tempor incididunt ut labore et dolore magna aliqua. Sed do eiusmod tempor incididunt ut labore et dolore magna aliqua. Lorem ipsum dolor sit amet, consectetur adipiscing elit, sed do eiusmod tempor incididunt ut labore. Ut enim ad minim veniam, quis nostrud exercitation ullamco laboris nisi ut aliquip.</p>
  </div>
  <footer class="foot"><div class="brand"><i></i><span>Corvath</span></div><div class="bar">CORVATH | Copyright ©</div><div class="num">9</div></footer>
</section>
<!-- 10 -->
<section class="slide">
  <h2 class="title" style="top:20px">Title And Body Slide</h2>
  <p style="position:absolute;left:16px;top:50px;font-size:6.5px;font-weight:500;color:var(--magenta)">Here Add Your Title</p>
  <div style="position:absolute;left:16px;right:16px;top:59px;border-top:.5px solid #ddd"></div>
  <div class="lorem" style="position:absolute;left:14px;right:16px;top:64px;display:grid;grid-template-columns:repeat(3,1fr);gap:7px">
    <div>• Lorem ipsum dolor sit amet, consectetur adipiscing elit, sed do eiusmod tempor incididunt ut labore.<br><br>• Ut enim ad minim veniam, quis nostrud exercitation ullamco laboris.<br><br>• Lorem ipsum dolor sit amet, consectetur adipiscing elit, sed do eiusmod.</div>
    <div>• Lorem ipsum dolor sit amet, consectetur adipiscing elit, sed do eiusmod tempor incididunt ut labore.<br><br>• Ut enim ad minim veniam, quis nostrud exercitation ullamco laboris.<br><br>• Lorem ipsum dolor sit amet, consectetur adipiscing elit, sed do eiusmod.</div>
    <div>• Lorem ipsum dolor sit amet, consectetur adipiscing elit, sed do eiusmod tempor incididunt ut labore.<br><br>• Ut enim ad minim veniam, quis nostrud exercitation ullamco laboris.<br><br>• Lorem ipsum dolor sit amet, consectetur adipiscing elit, sed do eiusmod.</div>
  </div>
  <footer class="foot"><div class="brand"><i></i><span>Corvath</span></div><div class="bar">CORVATH | Copyright ©</div><div class="num">10</div></footer>
</section>
<!-- 11 -->
<section class="slide">
  <div style="position:absolute;left:24px;top:30px;width:111px;height:96px;background:linear-gradient(135deg,var(--cyan),var(--purple))"></div>
  <div role="img" aria-label="Photo of a person typing on a laptop" style="position:absolute;left:0;top:20px;width:122px;height:81px;background:linear-gradient(135deg,#8a5a2e,#c89a5a 50%,#e6e2dc);box-shadow:0 2px 4px rgba(0,0,0,.3)"></div>
  <h2 class="title" style="left:146px;top:38px">Pic And Text</h2>
  <p class="lorem" style="position:absolute;left:146px;right:18px;top:64px">Lorem ipsum dolor sit amet, consectetur adipiscing elit, sed do eiusmod tempor incididunt ut labore et dolore magna aliqua. Lorem ipsum dolor sit amet, consectetur adipiscing elit, sed do eiusmod tempor incididunt ut labore et dolore magna aliqua. Ut enim ad minim veniam, quis nostrud exercitation ullamco laboris nisi ut aliquip.</p>
  <footer class="foot"><div class="brand"><i></i><span>Corvath</span></div><div class="bar">CORVATH | Copyright ©</div><div class="num">11</div></footer>
</section>
<!-- 12 -->
<section class="slide">
  <h2 class="title" style="top:10px">Title And Body Slide</h2>
  <div class="icon" style="left:15px;top:46px"></div><div style="position:absolute;left:29px;top:42px;width:80px"><p class="pname">Project name</p><p class="lorem">Lorem ipsum dolor sit amet, nec an dictas equidem appellantur, ut has commune. Mea illum, ludus solet idpro.</p></div>
  <div class="icon" style="left:129px;top:46px"></div><div style="position:absolute;left:143px;top:42px;width:80px"><p class="pname">Project name</p><p class="lorem">Lorem ipsum dolor sit amet, nec an dictas equidem appellantur, ut has commune. Mea illum, ludus solet idpro.</p></div>
  <div class="icon" style="left:15px;top:73px"></div><div style="position:absolute;left:29px;top:69px;width:80px"><p class="pname">Project name</p><p class="lorem">Lorem ipsum dolor sit amet, nec an dictas equidem appellantur, ut has commune. Mea illum, ludus solet idpro.</p></div>
  <div class="icon" style="left:129px;top:73px"></div><div style="position:absolute;left:143px;top:69px;width:80px"><p class="pname">Project name</p><p class="lorem">Lorem ipsum dolor sit amet, nec an dictas equidem appellantur, ut has commune. Mea illum, ludus solet idpro.</p></div>
  <div class="icon" style="left:15px;top:100px"></div><div style="position:absolute;left:29px;top:96px;width:80px"><p class="pname">Project name</p><p class="lorem">Lorem ipsum dolor sit amet, nec an dictas equidem appellantur, ut has commune. Mea illum, ludus solet idpro.</p></div>
  <div class="icon" style="left:129px;top:100px"></div><div style="position:absolute;left:143px;top:96px;width:80px"><p class="pname">Project name</p><p class="lorem">Lorem ipsum dolor sit amet, nec an dictas equidem appellantur, ut has commune. Mea illum, ludus solet idpro.</p></div>
  <footer class="foot"><div class="brand"><i></i><span>Corvath</span></div><div class="bar">CORVATH | Copyright ©</div><div class="num">12</div></footer>
</section>

<!-- 13 -->
<section class="slide">
  <h2 class="title center" style="top:10px">6 Columns Slide</h2>
  <div class="ring" style="left:21px;top:46px"></div><div style="position:absolute;left:43px;top:44px;width:75px"><p class="pname">Project name</p><p class="lorem">Lorem ipsum dolor sit amet, nec an dictas equidem appellantur, ut has commune. Mea illum, ludus solet idpro.</p></div>
  <div class="ring" style="left:135px;top:46px"></div><div style="position:absolute;left:157px;top:44px;width:75px"><p class="pname">Project name</p><p class="lorem">Lorem ipsum dolor sit amet, nec an dictas equidem appellantur, ut has commune. Mea illum, ludus solet idpro.</p></div>
  <div class="ring" style="left:21px;top:71px"></div><div style="position:absolute;left:43px;top:69px;width:75px"><p class="pname">Project name</p><p class="lorem">Lorem ipsum dolor sit amet, nec an dictas equidem appellantur, ut has commune. Mea illum, ludus solet idpro.</p></div>
  <div class="ring" style="left:135px;top:71px"></div><div style="position:absolute;left:157px;top:69px;width:75px"><p class="pname">Project name</p><p class="lorem">Lorem ipsum dolor sit amet, nec an dictas equidem appellantur, ut has commune. Mea illum, ludus solet idpro.</p></div>
  <div class="ring" style="left:21px;top:99px"></div><div style="position:absolute;left:43px;top:97px;width:75px"><p class="pname">Project name</p><p class="lorem">Lorem ipsum dolor sit amet, nec an dictas equidem appellantur, ut has commune. Mea illum, ludus solet idpro.</p></div>
  <div class="ring" style="left:135px;top:99px"></div><div style="position:absolute;left:157px;top:97px;width:75px"><p class="pname">Project name</p><p class="lorem">Lorem ipsum dolor sit amet, nec an dictas equidem appellantur, ut has commune. Mea illum, ludus solet idpro.</p></div>
  <footer class="foot"><div class="brand"><i></i><span>Corvath</span></div><div class="bar">CORVATH | Copyright ©</div><div class="num">13</div></footer>
</section>
<!-- 14 -->
<section class="slide">
  <h2 class="title center" style="top:16px">Here Goes Title Of This Slide</h2>
  <p class="lorem" style="position:absolute;left:28px;right:28px;top:48px;text-align:center">Lorem Ipsum the printing and typesetting industry. Lorem Ipsum has been the industry's standard dummy text ever since the 1500s, when an unknown printer took a galley of type and scrambled it to make a type specimen book. It has survived not only five centuries.</p>
  <div class="stat" style="left:22px"><b>1M</b><p class="lorem">Lorem Ipsum has been the industry's standard dummy text ever since the 1500s</p></div>
  <div class="stat" style="left:96px"><b>2022</b><p class="lorem">Lorem Ipsum has been the industry's standard dummy text ever since</p></div>
  <div class="stat" style="left:169px"><b>150+</b><p class="lorem">Lorem Ipsum has been the industry's standard dummy text ever since the 1500s</p></div>
  <footer class="foot"><div class="brand"><i></i><span>Corvath</span></div><div class="bar">CORVATH | Copyright ©</div><div class="num">14</div></footer>
</section>
<!-- 15 -->
<section class="slide">
  <div class="box" style="left:16px;top:12px;width:108px;height:53px;background:var(--cyan)"><h3>Text Here</h3><p class="lorem">Lorem ipsum dolor sit amet, consectetur adipiscing elit, sed do eiusmod tempor incididunt ut labore et dolore magna aliqua. Ut enim ad minim veniam, quis nostrud exercitation ullamco laboris nisi ut aliquip ex.</p></div>
  <p class="lorem" style="position:absolute;left:132px;right:14px;top:29px">Lorem ipsum dolor sit amet, consectetur adipiscing elit, sed do eiusmod tempor incididunt ut labore et dolore magna aliqua. Ut enim ad minim veniam, quis nostrud exercitation ullamco laboris nisi ut aliquip ex.</p>
  <p style="position:absolute;left:24px;top:81px;width:100px;font-size:9px;line-height:11px;font-weight:500">Lorem ipsum dolor sit amet consect adipiscing elit</p>
  <div class="box" style="left:130px;top:68px;width:106px;height:54px;background:var(--violet)"><h3>Text Here</h3><p class="lorem">Lorem ipsum dolor sit amet, consectetur adipiscing elit, sed do eiusmod tempor incididunt ut labore et dolore magna aliqua. Ut enim ad minim veniam, quis nostrud exercitation ullamco laboris nisi ut aliquip ex.</p></div>
  <footer class="foot"><div class="brand"><i></i><span>Corvath</span></div><div class="bar">CORVATH | Copyright ©</div><div class="num">15</div></footer>
</section>

<!-- 16 -->
<section class="slide">
  <div style="position:absolute;left:0;right:0;top:0;height:71px;background:linear-gradient(180deg,var(--cyan),#7b4fbf 70%,#9e3aa0)"></div>
  <h2 style="position:absolute;left:0;right:0;top:14px;text-align:center;color:#fff;font-size:12px;font-weight:500">Here Add Awesome Text</h2>
  <p class="lorem" style="position:absolute;left:36px;right:36px;top:41px;text-align:center;color:rgba(255,255,255,.8)">Lorem ipsum dolor sit amet, consectetur adipiscing elit, sed do eiusmod tempor incididunt ut labore et dolore magna aliqua. Lorem ipsum dolor sit amet, consectetur adipiscing elit.</p>
  <div style="position:absolute;left:39px;top:59px;width:23px;height:23px;border-radius:50%;background:var(--violet);border:2px solid #fff;box-shadow:0 1px 3px rgba(0,0,0,.3)"></div>
  <div style="position:absolute;left:112px;top:59px;width:23px;height:23px;border-radius:50%;background:var(--cyan);border:2px solid #fff;box-shadow:0 1px 3px rgba(0,0,0,.3)"></div>
  <div style="position:absolute;left:185px;top:59px;width:23px;height:23px;border-radius:50%;background:var(--navy);border:2px solid #fff;box-shadow:0 1px 3px rgba(0,0,0,.3)"></div>
  <div style="position:absolute;left:20px;top:88px;width:62px;text-align:center"><p class="pname">Project name</p><p class="lorem">Lorem ipsum dolor sit amet, nec an dictas equidem appellantur, ut has commune accommodare. Mea illum, ludus solet idpro.</p></div>
  <div style="position:absolute;left:93px;top:88px;width:62px;text-align:center"><p class="pname">Project name</p><p class="lorem">Lorem ipsum dolor sit amet, nec an dictas equidem appellantur, ut has commune accommodare. Mea illum, ludus solet idpro.</p></div>
  <div style="position:absolute;left:166px;top:88px;width:62px;text-align:center"><p class="pname">Project name</p><p class="lorem">Lorem ipsum dolor sit amet, nec an dictas equidem appellantur, ut has commune accommodare. Mea illum, ludus solet idpro.</p></div>
  <footer class="foot"><div class="brand"><i></i><span>Corvath</span></div><div class="bar">CORVATH | Copyright ©</div><div class="num">16</div></footer>
</section>
<!-- 17 -->
<section class="slide">
  <div role="img" aria-label="Image of glowing blue DNA strands" style="position:absolute;left:0;top:0;width:189px;height:95px;background:linear-gradient(135deg,#0a2a66,#1f78d6 45%,#0b3a8a)"></div>
  <div style="position:absolute;left:122px;top:41px;width:98px;height:62px;border-radius:5px;background:linear-gradient(180deg,#3fbdee,var(--navy));color:#fff;text-align:center;font-size:9px;line-height:11px;font-weight:500;padding-top:14px">Here is a place<br>for short<br>statement</div>
  <h2 style="position:absolute;left:19px;top:107px;font-size:14px;font-weight:500">Heading + Text + Image Slide</h2>
  <footer class="foot"><div class="brand"><i></i><span>Corvath</span></div><div class="bar">CORVATH | Copyright ©</div><div class="num">17</div></footer>
</section>
<!-- 18 -->
<section class="slide">
  <h2 class="title center" style="top:14px">3 Columns Slide</h2>
  <div class="card" style="left:34px;background:var(--cyan)"><h4>Project name here</h4><p class="lorem">Lorem ipsum dolor sit amet, nec an dictas equidem appellantur, ut has commune accommodare. Mea illum, ludus solet idpro.</p></div>
  <div class="card" style="left:98px;background:var(--violet)"><h4>Project name here</h4><p class="lorem">Lorem ipsum dolor sit amet, nec an dictas equidem appellantur, ut has commune accommodare. Mea illum, ludus solet idpro.</p></div>
  <div class="card" style="left:162px;background:var(--magenta)"><h4>Project name here</h4><p class="lorem">Lorem ipsum dolor sit amet, nec an dictas equidem appellantur, ut has commune accommodare. Mea illum, ludus solet idpro.</p></div>
  <div class="ring" style="left:56px;top:50px;width:15px;height:15px"></div>
  <div class="ring" style="left:120px;top:50px;width:15px;height:15px"></div>
  <div class="ring" style="left:184px;top:50px;width:15px;height:15px"></div>
  <footer class="foot"><div class="brand"><i></i><span>Corvath</span></div><div class="bar">CORVATH | Copyright ©</div><div class="num">18</div></footer>
</section>

<!-- 19 -->
<section class="slide">
  <h2 class="title center" style="top:12px">Table Slide</h2>
  <table>
    <thead><tr><th>Text</th><th>Text</th><th>Text</th><th>Text</th><th>Text</th></tr></thead>
    <tbody>
      <tr><td>Data</td><td>Data</td><td>Data</td><td>Data</td><td>Data</td></tr>
      <tr><td>Data</td><td>Data</td><td>Data</td><td>Data</td><td>Data</td></tr>
      <tr><td>Data</td><td>Data</td><td>Data</td><td>Data</td><td>Data</td></tr>
      <tr><td>Data</td><td>Data</td><td>Data</td><td>Data</td><td>Data</td></tr>
      <tr><td>Data</td><td>Data</td><td>Data</td><td>Data</td><td>Data</td></tr>
      <tr><td>Data</td><td>Data</td><td>Data</td><td>Data</td><td>Data</td></tr>
    </tbody>
  </table>
  <footer class="foot"><div class="brand"><i></i><span>Corvath</span></div><div class="bar">CORVATH | Copyright ©</div><div class="num">19</div></footer>
</section>
<!-- 20 -->
<section class="slide">
  <h2 class="title" style="left:22px;top:12px">Smart Art Slide</h2>
  <div class="ring" style="left:22px;top:45px;width:11px;height:11px"></div><div style="position:absolute;left:41px;top:42px;width:76px"><p class="pname">Project name</p><p class="lorem">Lorem ipsum dolor sit amet, nec an dictas equidem appellantur, ut has commune accommodare. Mea illum, ludus solet idpro.</p></div>
  <div class="ring" style="left:22px;top:72px;width:11px;height:11px"></div><div style="position:absolute;left:41px;top:69px;width:76px"><p class="pname">Project name</p><p class="lorem">Lorem ipsum dolor sit amet, nec an dictas equidem appellantur, ut has commune accommodare. Mea illum, ludus solet idpro.</p></div>
  <div class="ring" style="left:22px;top:99px;width:11px;height:11px"></div><div style="position:absolute;left:41px;top:96px;width:76px"><p class="pname">Project name</p><p class="lorem">Lorem ipsum dolor sit amet, nec an dictas equidem appellantur, ut has commune accommodare. Mea illum, ludus solet idpro.</p></div>
  <svg style="position:absolute;left:134px;top:22px" width="108" height="96" viewBox="0 0 108 96">
    <polygon points="54,2 80,45 28,45" fill="#3fc3ef" stroke="#3fc3ef" stroke-linejoin="round" stroke-width="3"/>
    <polygon points="25,52 52,52 52,94 3,94" fill="#b5289b" stroke="#b5289b" stroke-linejoin="round" stroke-width="3"/>
    <polygon points="56,52 83,52 105,94 56,94" fill="#2b2f8c" stroke="#2b2f8c" stroke-linejoin="round" stroke-width="3"/>
    <g font-family="Poppins,sans-serif" fill="#fff" text-anchor="middle">
      <text x="54" y="23" font-size="3.6" font-weight="600">Project</text><text x="54" y="27" font-size="3.6" font-weight="600">name</text>
      <text x="54" y="33" font-size="2.4" opacity=".8">Lorem ipsum dolor sit</text><text x="54" y="36" font-size="2.4" opacity=".8">amet, nec an dictas</text>
      <text x="33" y="69" font-size="3.6" font-weight="600">Project name</text>
      <text x="33" y="74" font-size="2.4" opacity=".8">Lorem ipsum dolor sit</text><text x="33" y="77" font-size="2.4" opacity=".8">amet, nec an dictas</text>
      <text x="76" y="69" font-size="3.6" font-weight="600">Project name</text>
      <text x="76" y="74" font-size="2.4" opacity=".8">Lorem ipsum dolor sit</text><text x="76" y="77" font-size="2.4" opacity=".8">amet, nec an dictas</text>
    </g>
  </svg>
  <footer class="foot"><div class="brand"><i></i><span>Corvath</span></div><div class="bar">CORVATH | Copyright ©</div><div class="num">20</div></footer>
</section>
<!-- 21 -->
<section class="slide">
  <h2 class="title center" style="top:10px">Infographic</h2>
  <div style="position:absolute;left:12px;top:45px;width:70px;text-align:right"><p class="pname">Project name</p><p class="lorem">Lorem ipsum dolor sit amet, nec an dictas equidem appellantur, ut has commune accommodare. Mea illum.</p></div>
  <div style="position:absolute;left:12px;top:95px;width:70px;text-align:right"><p class="pname">Project name</p><p class="lorem">Lorem ipsum dolor sit amet, nec an dictas equidem appellantur, ut has commune accommodare. Mea illum.</p></div>
  <div style="position:absolute;left:170px;top:45px;width:72px"><p class="pname">Project name</p><p class="lorem">Lorem ipsum dolor sit amet, nec an dictas equidem appellantur, ut has commune accommodare. Mea illum.</p></div>
  <div style="position:absolute;left:170px;top:95px;width:72px"><p class="pname">Project name</p><p class="lorem">Lorem ipsum dolor sit amet, nec an dictas equidem appellantur, ut has commune accommodare. Mea illum.</p></div>
  <svg style="position:absolute;left:86px;top:43px" width="80" height="80" viewBox="0 0 80 80">
    <g fill="none" stroke-width="16">
      <path d="M40 8 A32 32 0 0 0 8 40" stroke="#3fc3ef"/>
      <path d="M72 40 A32 32 0 0 0 40 8" stroke="#7d35a3"/>
      <path d="M8 40 A32 32 0 0 0 40 72" stroke="#7d35a3"/>
      <path d="M40 72 A32 32 0 0 0 72 40" stroke="#3fc3ef"/>
    </g>
    <circle cx="40" cy="40" r="23" fill="#fff"/>
    <circle cx="40" cy="40" r="19" fill="#fff" stroke="#ddd" stroke-width=".5"/>
    <text x="40" y="42" text-anchor="middle" font-family="Poppins,sans-serif" font-size="5.5" font-weight="500" fill="#7d35a3">Corvath</text>
  </svg>
  <footer class="foot"><div class="brand"><i></i><span>Corvath</span></div><div class="bar">CORVATH | Copyright ©</div><div class="num">21</div></footer>
</section>

<!-- 22 -->
<section class="slide">
  <h2 class="title center" style="top:12px">Here Add Your Title</h2>
  <p class="lorem" style="position:absolute;left:46px;right:46px;top:38px;text-align:center;color:var(--ink)">Lorem Ipsum the printing and typesetting industry. Lorem Ipsum has been the industry's standard dummy text ever since the 1500s, when an unknown printer took a galley of type and scrambled it to make a type specimen book. It has survived not only five centuries.</p>
  <svg style="position:absolute;left:0;top:62px" width="252" height="60" viewBox="0 0 252 60">
    <g fill="none" stroke-width="2.5" transform="rotate(-90)">
      <circle cx="-19" cy="73" r="16" stroke="#eee"/><circle cx="-19" cy="73" r="16" stroke="#3fc3ef" stroke-dasharray="50.3 100.5"/>
      <circle cx="-19" cy="126" r="16" stroke="#eee"/><circle cx="-19" cy="126" r="16" stroke="#7d35a3" stroke-dasharray="75.4 100.5"/>
      <circle cx="-19" cy="178" r="16" stroke="#eee"/><circle cx="-19" cy="178" r="16" stroke="#1e1e24" stroke-dasharray="40.2 100.5"/>
    </g>
    <g font-family="Poppins,sans-serif" font-size="11" font-weight="500" fill="#1e1e24" text-anchor="middle">
      <text x="73" y="23">50%</text><text x="126" y="23">75%</text><text x="178" y="23">40%</text>
    </g>
    <g font-family="Poppins,sans-serif" font-size="3.4" fill="#1e1e24" text-anchor="middle">
      <text x="73" y="47">Lorem ipsum dolor amet</text><text x="73" y="52">amet consectetur dolor</text>
      <text x="126" y="47">Lorem ipsum dolor amet</text><text x="126" y="52">amet consectetur dolor</text>
      <text x="178" y="47">Lorem ipsum dolor amet</text><text x="178" y="52">amet consectetur dolor</text>
    </g>
  </svg>
  <footer class="foot"><div class="brand"><i></i><span>Corvath</span></div><div class="bar">CORVATH | Copyright ©</div><div class="num">22</div></footer>
</section>
<!-- 23 -->
<section class="slide">
  <h2 class="title center" style="top:18px">Company Timeline</h2>
  <svg style="position:absolute;left:20px;top:55px" width="212" height="30" viewBox="0 0 212 30">
    <g font-family="Poppins,sans-serif" font-size="4" font-weight="600" fill="#fff" text-anchor="middle">
      <polygon points="0,3 38,3 47,14 38,26 0,26 8,14" fill="#3fc3ef"/><text x="25" y="16">STEP 01</text>
      <polygon points="40,3 78,3 87,14 78,26 40,26 48,14" fill="#7d35a3"/><text x="65" y="16">STEP 02</text>
      <polygon points="80,3 118,3 127,14 118,26 80,26 88,14" fill="#3fc3ef"/><text x="105" y="16">STEP 03</text>
      <polygon points="120,3 158,3 167,14 158,26 120,26 128,14" fill="#7d35a3"/><text x="145" y="16">STEP 04</text>
      <polygon points="160,3 198,3 207,14 198,26 160,26 168,14" fill="#3fc3ef"/><text x="185" y="16">STEP 05</text>
    </g>
  </svg>
  <div style="position:absolute;left:22px;right:18px;top:92px;display:grid;grid-template-columns:repeat(5,1fr);gap:4px;text-align:center">
    <div><p style="font-size:3.6px;font-weight:600">Project name</p><p class="lorem">Lorem Ipsum is simply dummy unknown printer took a galley of type and scrambled it.</p></div>
    <div><p style="font-size:3.6px;font-weight:600">Project name</p><p class="lorem">Lorem Ipsum is simply dummy unknown printer took a galley of type and scrambled it.</p></div>
    <div><p style="font-size:3.6px;font-weight:600">Project name</p><p class="lorem">Lorem Ipsum is simply dummy unknown printer took a galley of type and scrambled it.</p></div>
    <div><p style="font-size:3.6px;font-weight:600">Project name</p><p class="lorem">Lorem Ipsum is simply dummy unknown printer took a galley of type and scrambled it.</p></div>
    <div><p style="font-size:3.6px;font-weight:600">Project name</p><p class="lorem">Lorem Ipsum is simply dummy unknown printer took a galley of type and scrambled it.</p></div>
  </div>
  <footer class="foot"><div class="brand"><i></i><span>Corvath</span></div><div class="bar">CORVATH | Copyright ©</div><div class="num">23</div></footer>
</section>
<!-- 24 -->
<section class="slide" style="background:linear-gradient(135deg,#fafafc,#eeeef2)">
  <div class="brand" style="position:absolute;left:42px;top:20px;color:var(--purple)"><i></i><span>Corvath Therapeutics</span></div>
  <div class="contact" style="top:41px;background:linear-gradient(90deg,#5f6fd0,var(--violet));color:#fff">
    <svg width="6" height="6" viewBox="0 0 10 10"><circle cx="5" cy="5" r="4" fill="none" stroke="#fff"/><path d="M1 5h8M5 1v8" stroke="#fff" stroke-width=".8"/></svg>www.corvath-example.com</div>
  <div class="contact" style="top:58px">
    <svg width="6" height="6" viewBox="0 0 10 10"><path d="M5 9C2 6 2 5 2 4a3 3 0 016 0c0 1 0 2-3 5z" fill="none" stroke="#3f6fd6"/></svg>Here to write your<br>company address</div>
  <div class="contact" style="top:75px">
    <svg width="6" height="6" viewBox="0 0 10 10"><path d="M2 1l2 0 1 2-1.5 1a6 6 0 003 3L7.5 5.5l2 1v2A8 8 0 011 1z" fill="#3f6fd6"/></svg>(555) 010 0199</div>
  <div class="contact" style="top:93px">
    <svg width="6" height="6" viewBox="0 0 10 10"><rect x="1" y="2" width="8" height="6" fill="#3f6fd6"/><path d="M1 2l4 3 4-3" fill="none" stroke="#fff" stroke-width=".7"/></svg>hello@corvath-example.com</div>
  <div style="position:absolute;left:57px;top:114px;display:flex;gap:2px">
    <i style="width:4px;height:4px;border-radius:50%;background:var(--ink)"></i><i style="width:4px;height:4px;border-radius:50%;background:var(--ink)"></i><i style="width:4px;height:4px;border-radius:50%;background:var(--ink)"></i><i style="width:4px;height:4px;border-radius:50%;background:var(--ink)"></i>
  </div>
  <p style="position:absolute;left:136px;top:60px;font-size:15px;font-weight:600;color:#5a4fc0">Thank You</p>
</section>

</main>
</body>
</html>
```